Book Cover for: TITLE Mend the Quiet Hours SUBTITLE For partners who choose to stay together

We need a full cover design for a book on relationships written by husband and wife team, Marla and Walter Dunmore, PhD. This book will offer hope for couples that are on the verge of breaking up but want to work things out and stay together. The theme is to teach couples about their own reactions to their partner, how moods affect a relationship, how to get creative to solving problems and how to have a good feeling towards your partner regardless of differences. This book is about hope. It is a positive look at relationships that feel hopeless.

Target Market(s)

Married or couples that are going through a difficult time and are considering splitting up due to, communication difficulties, addiction, affair. We imagine the book will appeal to women more than men but still want a cover that men would be comfortable picking up.

Colors

Designer to choose colors to be used in the design.

Requirements
Must have
• We want the cover to beautiful, intriguing, simple and uncomplicated. We don't want it overly busy, technical, or complex.
Nice to have
• MAYBE?? a broken heart being put back together.
Should not have
• No photo, no cartoon, no flowers, no couple (unless obscure and not gender specific).

```html
<!DOCTYPE html>
<html lang="en">
<head>
<meta charset="utf-8">
<title>Mend the Quiet Hours — Book Cover</title>
<link href="https://fonts.googleapis.com/css2?family=Bebas+Neue&family=Oswald:wght@300;500;600&display=swap" rel="stylesheet">
<style>
  :root {
    --backdrop: #1d1d1d;
    --paper: #f2f1ed;
    --ink: #0d0d0d;
    --heart-pink: #ff0a50;
    --scribble-grey: #9a9a9a;
  }
  html, body {
    margin: 0;
    padding: 0;
    width: 1200px;
    height: 878px;
    overflow: hidden;
    background: var(--backdrop);
  }
  .stage {
    position: relative;
    width: 1200px;
    height: 878px;
    background: var(--backdrop);
  }
  .book-cover {
    position: absolute;
    left: 366px;
    top: 63px;
    width: 470px;
    height: 751px;
    background: var(--paper);
    box-shadow: 0 0 40px rgba(0,0,0,0.45);
    overflow: hidden;
  }
  .cover-title {
    position: absolute;
    left: 0;
    right: 0;
    top: 34px;
    margin: 0;
    text-align: center;
    font-family: "Bebas Neue", "Oswald", sans-serif;
    font-weight: 400;
    font-size: 92px;
    line-height: 75px;
    letter-spacing: 1px;
    color: var(--ink);
    white-space: nowrap;
  }
  .cover-title .title-line { display: block; }
  .cover-title .title-accent { color: var(--heart-pink); }
  .cover-subtitle {
    position: absolute;
    left: 0;
    right: 0;
    top: 189px;
    margin: 0;
    text-align: center;
    font-family: "Oswald", sans-serif;
    font-weight: 300;
    font-size: 18px;
    letter-spacing: 0.2px;
    color: var(--ink);
    text-transform: uppercase;
    white-space: nowrap;
  }
  .cover-subtitle strong { font-weight: 600; }
  .cover-artwork {
    position: absolute;
    left: 10px;
    top: 229px;
    width: 456px;
    height: 464px;
    border-radius: 50%;
    background: radial-gradient(ellipse at 50% 50%,
      var(--heart-pink) 0%,
      var(--heart-pink) 42%,
      rgba(154,154,154,0.55) 58%,
      rgba(154,154,154,0.15) 72%,
      rgba(242,241,237,0) 80%);
  }
  .cover-authors {
    position: absolute;
    left: 0;
    right: 0;
    top: 698px;
    margin: 0;
    text-align: center;
    font-family: "Oswald", sans-serif;
    font-weight: 500;
    font-size: 20px;
    letter-spacing: 3.6px;
    color: var(--ink);
    text-transform: uppercase;
    white-space: nowrap;
  }
</style>
</head>
<body>
  <main class="stage">
    <article class="book-cover">
      <h1 class="cover-title">
        <span class="title-line">Mend the</span>
        <span class="title-line">Quiet <span class="title-accent">Hours</span></span>
      </h1>
      <p class="cover-subtitle">For partners who <strong>choose to stay together</strong></p>
      <div class="cover-artwork" role="img" aria-label="Red paper heart split down the middle and held together with strips of tape, set on a tangle of dark scribbled lines"></div>
      <p class="cover-authors">Marla and Walter Dunmore, PhD</p>
    </article>
  </main>
</body>
</html>
```